Property Service business needs a cool business card

Looking for an eloquent and unique business card using the logo and colours attached as uploaded files.

Target Market(s)

Body corporates, real estate agents, building managers

Industry/Entity Type

Business

Contact Information for Business Card

- Quorvel Logo
- Construction * Maintenance * Remedial

- Tom Wexley
- Business Manager

- Ph 0417586204
- P.O Box 461 South Melbourne Vic 3090
- Email tom@quorvel.com
- Website www.quorvelpropertyservices.com.au

Requirements
Must have
• Clean and fresh look, colours must be vibrant!
Nice to have
• unique features
Should not have
• Should not be overcrowded

```html
<!DOCTYPE html>
<html lang="en">
<head>
<meta charset="utf-8">
<title>Quorvel Property Services – Business Card</title>
<link href="https://fonts.googleapis.com/css2?family=Jura:wght@400;500;600&display=swap" rel="stylesheet">
<style>
  :root {
    --stage: #1b1b1b;
    --card-edge: #2b3440;
    --blue-top: #24558f;
    --teal-mid: #2a5d6c;
    --blue-bottom: #152f59;
    --white: #f4f4f4;
    --green: #8bc34a;
    --monogram: #2e62a2;
  }
  * { margin: 0; padding: 0; box-sizing: border-box; }
  html, body {
    width: 1200px; height: 361px; overflow: hidden;
    background: var(--stage);
    font-family: "Jura", "Century Gothic", sans-serif;
  }
  .card {
    position: absolute; top: 21px;
    width: 574px; height: 327px;
    overflow: hidden;
    outline: 1px solid var(--card-edge);
  }
  .card--front { left: 17px; }
  .card--back { left: 606px; }
  .card__bg {
    position: absolute; inset: 0;
    background: linear-gradient(160deg, var(--blue-top) 0%, var(--teal-mid) 50%, var(--blue-bottom) 100%);
  }
  .monogram {
    position: absolute; top: 10px; right: 16px;
    font-size: 32px; font-weight: 600; letter-spacing: 1px;
    color: var(--monogram);
  }
  .brand-mark {
    position: absolute; left: 86px; top: 138px;
    display: flex; align-items: center; gap: 12px;
    font-size: 46px; font-weight: 500; color: var(--white);
  }
  .brand-mark__square { width: 26px; height: 26px; background: var(--green); }
  .contact { position: absolute; left: 322px; top: 113px; }
  .contact__name {
    font-size: 35px; font-weight: 500; color: var(--white);
    line-height: 1; margin-bottom: 8px; margin-left: -3px;
  }
  .contact__line { font-size: 14.5px; color: var(--green); line-height: 17px; }
  .contact__gap { height: 6px; }
  .footer {
    position: absolute; left: 14px; bottom: 16px;
    display: flex; align-items: center; gap: 16px;
  }
  .footer__brand {
    display: flex; align-items: center; gap: 8px;
    font-size: 32px; font-weight: 500; color: var(--white);
  }
  .footer__square { width: 16px; height: 16px; background: var(--green); }
  .footer__info { line-height: 16px; }
  .footer__services { font-size: 14.5px; color: var(--green); }
  .footer__web { font-size: 14px; color: var(--white); }
</style>
</head>
<body>
  <section class="card card--front">
    <div class="card__bg" role="img" aria-label="Background of angled blue and teal bands"></div>
    <div class="monogram">TW</div>
    <div class="brand-mark"><span class="brand-mark__square"></span>Quorvel</div>
    <div class="contact">
      <h1 class="contact__name">Tom Wexley</h1>
      <p class="contact__line">(04) 1758 6204</p>
      <div class="contact__gap"></div>
      <p class="contact__line">P.O. Box 461</p>
      <p class="contact__line">Kellbrook VIC 3188</p>
      <div class="contact__gap"></div>
      <p class="contact__line">tom@quorvel.com</p>
    </div>
  </section>

  <section class="card card--back">
    <div class="card__bg" role="img" aria-label="Background of angled blue and teal bands"></div>
    <div class="monogram">TW</div>
    <div class="footer">
      <div class="footer__brand"><span class="footer__square"></span>Quorvel</div>
      <div class="footer__info">
        <p class="footer__services">Construction | Maintenance | Remdial</p>
        <p class="footer__web">www.quorvelpropertyservices.com.au</p>
      </div>
    </div>
  </section>
</body>
</html>
```